TILVERA.COM is a premium domain sales company. Our competitors are companies like brankoport.com, selvatrix.com, quimbelstock.com. Our current site is at www.tilveras.com.

We want to have the ability to search for domains, to highlight special offers and have some testimonials on the index page.

The logo for the site is attached.

Please be sure that the order form fits on the screen without scrolling the page. I want the entire form, including the submit button to fit without any page scrolling.

Delivered product - INDEX PAGE, ORDER FORM AND CONTENT PAGE PSDs.

Target Market(s)

Small to Medium business professionals

Industry/Entity Type

It Company

Requirements
Must have
• 1. List of domains for sale
2. Simple search box with button to run the search
3. link for advanced search
4. testimonial area. Note - this can be a small box where a different testimonial is displayed on each page load.
Nice to have
• Would like the site to have some white space. Don't want a heavily packed website. Give it an "airy" feel.

```html
<!DOCTYPE html>
<html lang="en">
<head>
<meta charset="utf-8">
<title>Tilvera – Premium Domains</title>
<link rel="stylesheet" href="https://fonts.googleapis.com/css2?family=Arimo:wght@400;700&display=swap">
<style>
:root{
  --brand-blue:#0d4f95;
  --hero-deep:#0b6fae;
  --hero-mid:#2a9fd6;
  --hero-light:#3fc0e6;
  --heading-navy:#103a6b;
  --domain-green:#0b6a3e;
  --text-dark:#222;
  --text-grey:#444;
  --panel:#f6f6f6;
  --footer:#d4d4d4;
  --link-blue:#1d5fa8;
}
*{box-sizing:border-box;margin:0;padding:0}
html,body{width:1200px;height:961px;overflow:hidden}
body{position:relative;background:#fff;font-family:"Arimo",Arial,sans-serif;color:var(--text-dark)}
.abs{position:absolute}

.site-header{position:absolute;left:0;top:0;width:1200px;height:66px;background:linear-gradient(#fdfdfd,#e6e6e6)}
.brand{position:absolute;left:188px;top:16px;font-size:36px;font-weight:700;color:var(--brand-blue);letter-spacing:-0.5px}
.main-nav{position:absolute;left:531px;top:19px;width:422px;height:38px;border:1px solid #b9b9b9;border-radius:5px;background:linear-gradient(#fbfbfb,#d9d9d9);display:flex;box-shadow:0 1px 2px rgba(0,0,0,.2)}
.main-nav a{flex:1;text-align:center;line-height:36px;font-size:17px;color:#111;text-decoration:none;border-left:1px solid #a8a8a8}
.main-nav a:first-child{border-left:none}

.hero{position:absolute;left:0;top:66px;width:1200px;height:352px;background:radial-gradient(ellipse 420px 260px at 620px 200px,var(--hero-light),var(--hero-mid) 55%,var(--hero-deep))}
.hero h1{position:absolute;left:190px;top:64px;font-size:33px;font-weight:400;color:var(--heading-navy)}
.hero .lede{position:absolute;left:190px;top:120px;font-size:15px;color:#eaf6fc}
.search{position:absolute;left:190px;top:150px;width:361px;height:43px}
.search .field{position:absolute;left:0;top:0;width:310px;height:43px;background:#fff;border-radius:5px 0 0 5px;border:1px solid #bcd}
.search .go{position:absolute;left:310px;top:0;width:51px;height:43px;border-radius:0 5px 5px 0;background:linear-gradient(#f4f4f4,#cfcfcf);border:1px solid #aaa}
.advance{position:absolute;left:190px;top:288px;font-size:19px;color:#fff;display:flex;align-items:center;gap:6px}
.advance span{border-bottom:1px dashed #fff}
.offer{position:absolute;left:818px;top:0}
.testimonials h2{position:absolute;left:627px;top:96px;font-size:32px;font-weight:400;color:var(--heading-navy)}
.testimonials .sub{position:absolute;left:628px;top:142px;font-size:15px;color:var(--heading-navy)}
.testimonials .source{position:absolute;right:237px;top:183px;font-size:15px;font-weight:700;color:var(--heading-navy)}
.testimonials blockquote{position:absolute;left:629px;top:206px;width:335px;font-size:14px;line-height:17.5px;color:var(--heading-navy)}
.testimonials .date{position:absolute;right:237px;top:276px;font-size:14px;font-weight:700;color:var(--heading-navy)}
.dots{position:absolute;left:556px;top:323px;display:flex;gap:16px}
.dots i{width:16px;height:16px;border-radius:50%;background:radial-gradient(circle at 50% 35%,#3b86c5,#0b3f78);box-shadow:0 1px 2px rgba(0,0,0,.4)}
.dots i.on{background:radial-gradient(circle at 50% 35%,#fff,#bdbdbd)}

.content{position:absolute;left:176px;top:418px;width:803px;height:459px;background:linear-gradient(#fdfdfd,var(--panel))}
.domain{position:absolute;width:240px;text-align:center;color:var(--domain-green)}
.domain .name{font-size:23px}
.domain .price{font-size:19px;margin-top:10px}
.submit{display:inline-block;margin-top:10px;width:101px;height:30px;line-height:28px;border:1px solid #b3b3b3;border-radius:3px;background:linear-gradient(#fff,#e1e1e1);font-size:15px;font-weight:700;color:#333;box-shadow:0 1px 2px rgba(0,0,0,.25);position:relative}
.submit::before{content:"";position:absolute;left:0;bottom:0;border-left:10px solid #8cc63f;border-top:10px solid transparent}
.all-domains{position:absolute;left:756px;top:680px;font-size:19px;color:var(--domain-green);display:flex;align-items:center;gap:6px}

.reviews{position:absolute;left:189px;top:718px;width:781px;height:177px;border:1px solid #bdbdbd;border-radius:5px;background:linear-gradient(#f5f5f5,#e4e4e4)}
.review{position:absolute;display:flex;gap:14px}
.review .photo{width:58px;height:48px;border:2px solid #fff;box-shadow:0 0 2px #999;flex:none}
.review .who{font-size:14px;color:var(--link-blue)}
.review p{font-size:14px;line-height:18px;color:#222}

.site-footer{position:absolute;left:0;top:877px;width:1200px;height:84px;background:linear-gradient(#bdbdbd,#e3e3e3 40%,#d0d0d0)}
.copy{position:absolute;left:205px;top:50px;font-size:15px;color:var(--link-blue)}
.address{position:absolute;left:648px;top:24px;font-size:15px;line-height:18px;color:var(--link-blue)}
</style>
</head>
<body>
<header class="site-header">
  <div class="brand">TILVERA.COM</div>
  <nav class="main-nav"><a>Home</a><a>Faqs</a><a>About Us</a><a>Contact</a></nav>
</header>

<section class="hero">
  <h1>Find Your Domain</h1>
  <p class="lede">You can find the best name for your business...</p>
  <div class="search">
    <div class="field"></div>
    <div class="go">
      <svg width="49" height="41" viewBox="0 0 49 41"><circle cx="23" cy="18" r="7" fill="none" stroke="#333" stroke-width="3"/><line x1="28" y1="23" x2="33" y2="28" stroke="#333" stroke-width="4" stroke-linecap="round"/></svg>
    </div>
  </div>
  <div class="advance">
    <svg width="22" height="16" viewBox="0 0 22 16"><path d="M2 6h7l-2-4h2l4 4h7a1.5 1.5 0 0 1 0 3h-4v1.5h-3V12h-2v2H4L2 12z" fill="none" stroke="#fff" stroke-width="1.4"/></svg>
    <span>Advance Search</span>
  </div>

  <svg class="offer" width="117" height="112" viewBox="0 0 117 112">
    <defs><linearGradient id="ribbon" x1="0" y1="0" x2="0" y2="1"><stop offset="0" stop-color="#3fb6ef"/><stop offset="1" stop-color="#1a7fd0"/></linearGradient></defs>
    <path d="M2 0h113v80L58.5 110 2 80z" fill="url(#ribbon)" stroke="#b8e6ff" stroke-width="3"/>
    <text x="58.5" y="36" text-anchor="middle" font-family="Arimo,Arial,sans-serif" font-size="27" fill="#0c3a66">30%</text>
    <text x="58.5" y="72" text-anchor="middle" font-family="Arimo,Arial,sans-serif" font-size="27" fill="#0c3a66">OFF</text>
  </svg>

  <div class="testimonials">
    <h2>Testimonials</h2>
    <p class="sub">what people are saying about us...</p>
    <p class="source">FOLIOHALL.COM</p>
    <blockquote><b>John:</b> Lorem Ipsum is simply dummy text of the printing and typesetting industry. Lorem Ipsum has been theindustry's standard dummy text ever since the 1500s,</blockquote>
    <p class="date">May 28, 2013 12:00 am</p>
  </div>
  <div class="dots"><i></i><i></i><i></i><i class="on"></i></div>
</section>

<main class="content"></main>

<div class="domain" style="left:168px;top:436px"><div class="name">remedyleaf.com</div><div class="price">Health &nbsp;$8700.00</div><span class="submit">SUBMIT</span></div>
<div class="domain" style="left:452px;top:436px"><div class="name">sprintkits.com</div><div class="price">Sports &nbsp;&nbsp;&nbsp; $5000.00</div><span class="submit">SUBMIT</span></div>
<div class="domain" style="left:752px;top:436px"><div class="name">motor-vintage.com</div><div class="price">Vehicals &nbsp;$100.00</div><span class="submit">SUBMIT</span></div>
<div class="domain" style="left:168px;top:560px"><div class="name">everyhomestead.com</div><div class="price">Real Estate &nbsp;$ 999.00</div><span class="submit">SUBMIT</span></div>
<div class="domain" style="left:452px;top:560px"><div class="name">press-q.com</div><div class="price">Media &nbsp;$ 197.00</div><span class="submit">SUBMIT</span></div>
<div class="domain" style="left:752px;top:560px"><div class="name">plainloanpath.com</div><div class="price">Finance &nbsp;&nbsp;&nbsp;&nbsp; $ 300.00</div><span class="submit">SUBMIT</span></div>

<div class="all-domains">Search All Domains
  <svg width="16" height="14" viewBox="0 0 16 14"><path d="M2 2l5 5-5 5M8 2l5 5-5 5" fill="none" stroke="#222" stroke-width="2.4"/></svg>
</div>

<section class="reviews">
  <div class="review" style="left:12px;top:16px"><div class="photo" role="img" aria-label="Portrait photo of Selena" style="background:linear-gradient(#c9d3dc,#6a7d92)"></div><div><div class="who">Selena</div><p>“Lorem Ipsum is simply dummy text of<br>&nbsp;the printing and typesetting industry. “</p></div></div>
  <div class="review" style="left:426px;top:14px"><div class="photo" role="img" aria-label="Portrait photo of John" style="background:linear-gradient(#eee,#8a6a55)"></div><div><div class="who">John</div><p>“Lorem Ipsum is simply dummy text of<br>&nbsp;&nbsp;&nbsp;&nbsp;&nbsp;&nbsp;&nbsp;&nbsp;&nbsp;&nbsp;&nbsp;the printing and typesetting industry. “</p></div></div>
  <div class="review" style="left:12px;top:98px"><div class="photo" role="img" aria-label="Portrait photo of Jully" style="background:linear-gradient(#f1f1f1,#7a2a2a)"></div><div><div class="who">Jully</div><p>“Lorem Ipsum is simply dummy text of<br>&nbsp;&nbsp;&nbsp;&nbsp;&nbsp;&nbsp;&nbsp;&nbsp;&nbsp;&nbsp;the printing and typesetting industry. “</p></div></div>
  <div class="review" style="left:426px;top:96px"><div class="photo" role="img" aria-label="Portrait photo of Monica" style="background:linear-gradient(#f6f6f6,#b89a86)"></div><div><div class="who">Monica</div><p>“Lorem Ipsum is simply dummy text of<br>&nbsp;&nbsp;&nbsp;&nbsp;the printing and typesetting industry. “</p></div></div>
</section>

<footer class="site-footer">
  <p class="copy">© 2013 Tilvera, All Right Reserved. Privacy Policy</p>
  <p class="address">Tilvera, Inc. 4100 Orchard Lane Suite<br>&nbsp;210 &nbsp;Marlow, OR 97402 &nbsp;United States<br>+1 555.014.2290</p>
</footer>
</body>
</html>
```